design a catchy flyer for my electrical buisness

need a flyer designed to attract people to my business by looking professional and offering specials

Target Market(s)

all people i want to look affordable to everyone but still keeping that professional look and feel

Industry/Entity Type

Electrical

Requirements
Must have
• NO JOB TO BIG OR SMALL
• CALL NOW FOR A FREE QUOTE 0400318726
• NO CALL OUT FEE
• same promises as uploaded pic maybe written different style
• Your neighborhood electrician
• 100% satisfaction guaranteed
• were here to help
• mention this flyer for 10% off
• specializing in house renovations, extensions, kitchen and bathroom upgrades switchboard upgrades
• Make your house safe with our RCD and smoke alarm packages
Nice to have
• modern
• proffesional
• shows trust when customers read it
Should not have
• corny slogans
• cheap look

```html
<!DOCTYPE html>
<html lang="en">
<head>
<meta charset="UTF-8">
<title>VoltBridge Electrical Flyer</title>
<link href="https://fonts.googleapis.com/css2?family=Arimo:wght@400;700&display=swap" rel="stylesheet">
<style>
  :root {
    --orange: #f7931e;
    --ink: #3a3a3a;
    --panel: #5b5b5b;
    --band: #4a4a4a;
    --white: #ffffff;
  }
  html, body { margin: 0; padding: 0; overflow: hidden; background: var(--white); }
  .flyer {
    position: relative;
    width: 849px;
    height: 1200px;
    overflow: hidden;
    background: var(--white);
    font-family: "Arimo", Arial, sans-serif;
    color: var(--ink);
  }
  .brand {
    position: absolute; left: 28px; top: 26px;
    display: flex; align-items: center; gap: 18px;
  }
  .brand-dot { width: 84px; height: 84px; border-radius: 50%; background: var(--orange); }
  .brand-rule { width: 2px; height: 70px; background: #cfcfcf; }
  .brand-name { font-size: 40px; font-weight: 700; color: var(--orange); }
  .hero-photo {
    position: absolute; left: 400px; top: 0; width: 449px; height: 720px;
    background: radial-gradient(ellipse at 55% 40%, #f6d28a 0%, #e8c27a 30%, #c9c2b6 60%, #ffffff 95%);
  }
  .headline-block {
    position: absolute; left: 0; top: 164px; width: 440px; height: 90px;
    background: var(--orange);
  }
  .headline-block span {
    position: absolute; left: 30px; top: 6px;
    font-size: 80px; font-weight: 700; color: var(--white); line-height: 1;
  }
  .headline-sub {
    position: absolute; left: 30px; top: 266px;
    font-size: 50px; font-weight: 400; color: var(--ink); line-height: 1;
  }
  .no-fee {
    position: absolute; left: 30px; top: 322px;
    font-size: 34px; font-weight: 400; color: var(--orange); line-height: 1;
  }
  .guarantee {
    position: absolute; left: 28px; top: 382px; width: 242px; height: 158px;
    background: var(--orange); border-radius: 10px;
    box-sizing: border-box; padding-top: 16px;
    text-align: center;
    font-size: 38px; font-weight: 700; color: var(--white); line-height: 1.15;
  }
  .help {
    position: absolute; left: 28px; top: 556px;
    font-size: 52px; font-weight: 400; color: var(--ink); line-height: 1;
  }
  .offer-panel {
    position: absolute; left: 28px; top: 628px; width: 807px; height: 345px;
    background: var(--panel); border-radius: 12px;
  }
  .discount {
    position: absolute; left: 20px; top: 40px; width: 190px; height: 265px;
    box-sizing: border-box; padding-top: 30px;
    background: var(--orange); border-radius: 10px;
    text-align: center;
    font-size: 36px; color: var(--white); line-height: 1.4;
  }
  .discount p { margin: 0; }
  .discount strong { font-weight: 700; }
  .services {
    position: absolute; left: 232px; top: 44px; width: 560px; height: 115px;
    box-sizing: border-box; padding: 8px 14px;
    background: var(--white); border: 4px solid var(--orange); border-radius: 4px;
    font-size: 27px; color: var(--ink); line-height: 1.2;
  }
  .safety {
    position: absolute; left: 232px; top: 178px; width: 560px;
    font-size: 33px; font-weight: 700; color: var(--white); line-height: 1.25;
  }
  .tagline-band {
    position: absolute; left: 28px; top: 985px; width: 807px; height: 44px;
    background: var(--band);
    display: flex; align-items: center; justify-content: center;
    font-size: 29px; font-weight: 700; letter-spacing: 2px; color: var(--white);
  }
  .cta {
    position: absolute; left: 28px; top: 1045px;
    font-size: 40px; color: var(--ink); line-height: 1;
  }
  .phone {
    position: absolute; left: 28px; top: 1098px;
    font-size: 76px; font-weight: 700; color: var(--orange); line-height: 1; letter-spacing: 1px;
  }
</style>
</head>
<body>
<main class="flyer">
  <div class="hero-photo" role="img" aria-label="Smiling electrician in hard hat and tool belt holding a toolbox"></div>

  <header class="brand">
    <div class="brand-dot"></div>
    <div class="brand-rule"></div>
    <div class="brand-name">VoltBridge</div>
  </header>

  <div class="headline-block"><span>NO JOB</span></div>
  <div class="headline-sub">TO BIG OR SMALL</div>
  <div class="no-fee">NO CALL OUT FEE</div>

  <div class="guarantee">100%<br>satisfaction<br>guaranteed</div>

  <div class="help">Were here to help</div>

  <section class="offer-panel">
    <div class="discount">
      <p>Mention</p>
      <p>this flyer</p>
      <p>for</p>
      <p><strong>10% off</strong></p>
    </div>
    <div class="services">Specializing in house renovations, extensions, kitchen and bathroom upgrades switchboard upgrades</div>
    <div class="safety">Make your house safe with our RCD and smoke alarm packages</div>
  </section>

  <div class="tagline-band">Your Neighborhood Electrician</div>

  <div class="cta">CALL NOW FOR A FREE QUOTE</div>
  <div class="phone">0400318726</div>
</main>
</body>
</html>
```